Mirela Causo Photography

I need a website design for my photography business, I want something clean, elegant, Classy.. I like the colors, White, Black, Green/Blue, Pink, Brown, Lavender,, I have a lot added my Logo .... Additional Info... I need a Photography Website Design, with probably 6 Tabs, Home, About Me, Portfolio, Gallery, Investment, Contact.
Home Page should have my logo, Name & Address, Social Media Icons, and Pictures.
As long as the templates are made I have a hosting coming that will code it.
Target Market(s)
Portraits Photography, Senior Portraits, Newborn, Families, Events, Engagements, Wedding,
Industry/Entity Type
Business
Number of Pages Required
5+ page
Look and feel

```html
<!DOCTYPE html>
<html lang="en">
<head>
<meta charset="utf-8">
<title>Mirela Causo Photography</title>
<link rel="stylesheet" href="https://fonts.googleapis.com/css2?family=Fira+Sans:wght@300;400&family=Fira+Sans+Condensed:wght@600&display=swap">
<style>
  :root {
    --page-bg: #ffffff;
    --ink: #333333;
    --brand-purple: #8e2a8c;
    --accent-orange: #f08a4b;
    --panel: #f5f7f7;
    --hero-dark: #1e1d1c;
    --hero-mid: #3c3835;
    --hero-stone: #4a4642;
    --window-blue: rgba(118, 134, 160, 0.55);
    --band-plum: rgba(92, 36, 74, 0.55);
    --band-plum-deep: rgba(58, 20, 44, 0.65);
    --white: #ffffff;
  }
  * { margin: 0; padding: 0; box-sizing: border-box; }
  html, body { width: 1200px; height: 651px; overflow: hidden; background: var(--page-bg); }
  body { position: relative; font-family: "Fira Sans", sans-serif; color: var(--ink); }

  .brand {
    position: absolute; left: 62px; top: 26px; width: 136px;
    display: flex; flex-direction: column; align-items: center;
  }
  .brand-dot { width: 32px; height: 32px; border-radius: 50%; background: var(--ink); margin-bottom: 6px; }
  .brand-name {
    font-weight: 300; font-size: 17px; line-height: 19px;
    color: var(--ink); text-align: center;
  }

  .main-nav { position: absolute; left: 286px; top: 73px; display: flex; gap: 21px; }
  .main-nav a {
    display: block; padding: 2px 9px; font-size: 15px; line-height: 19px;
    color: var(--ink); text-decoration: none; letter-spacing: 0.3px;
  }
  .main-nav a.is-active { background: var(--brand-purple); color: var(--white); }
  .main-nav a.is-highlight { color: var(--accent-orange); }

  .hero {
    position: absolute; left: 41px; top: 117px; width: 1116px; height: 534px;
    overflow: hidden;
  }
  .hero-photo {
    position: absolute; inset: 0;
    background:
      linear-gradient(180deg, rgba(0,0,0,0) 0%, rgba(0,0,0,0) 60.5%, var(--band-plum) 61%, var(--band-plum-deep) 100%),
      radial-gradient(ellipse 260px 90px at 58% 88%, rgba(160,118,128,0.35), rgba(0,0,0,0) 75%),
      radial-gradient(ellipse 110px 170px at 46% 50%, var(--window-blue), rgba(0,0,0,0) 72%),
      radial-gradient(ellipse 400px 260px at 14% 34%, rgba(112,102,92,0.5), rgba(0,0,0,0) 72%),
      radial-gradient(ellipse 220px 300px at 72% 40%, rgba(100,96,90,0.35), rgba(0,0,0,0) 72%),
      linear-gradient(90deg, rgba(0,0,0,0.15) 0%, rgba(0,0,0,0) 20%, rgba(0,0,0,0) 72%, rgba(0,0,0,0.45) 100%),
      linear-gradient(180deg, var(--hero-dark) 0%, var(--hero-mid) 45%, var(--hero-stone) 60%, var(--hero-dark) 100%);
  }
  .hero-copy { position: absolute; left: 0; top: 46px; width: 1020px; text-align: center; color: var(--white); }
  .hero-title { font-weight: 400; font-size: 50px; line-height: 56px; letter-spacing: 1px; }
  .hero-tagline {
    margin-top: 12px; font-family: "Fira Sans Condensed", sans-serif;
    font-weight: 600; font-size: 16.5px;
  }
  .search-button {
    position: absolute; right: 88px; top: 0; width: 45px; height: 45px;
    background: var(--white); display: flex; align-items: center; justify-content: center;
  }

  .content-card { position: absolute; top: 445px; height: 100px; background: var(--panel); }
  .content-card.side { left: 22px; width: 317px; }
  .content-card.wide { left: 356px; width: 735px; }
</style>
</head>
<body>
  <header>
    <div class="brand">
      <span class="brand-dot"></span>
      <span class="brand-name">Mirela Causo Photography</span>
    </div>
    <nav class="main-nav">
      <a href="#">Menu Links</a>
      <a href="#">Menu Links</a>
      <a href="#" class="is-active">Menu Links</a>
      <a href="#">Menu Links</a>
      <a href="#">Menu Links</a>
      <a href="#" class="is-highlight">Menu Links</a>
    </nav>
  </header>

  <section class="hero">
    <div class="hero-photo" role="img" aria-label="Portrait of a woman in a black dress standing in a dark abandoned industrial hall with city light through the far windows"></div>
    <div class="hero-copy">
      <h1 class="hero-title">Photgraphy you will love.</h1>
      <p class="hero-tagline">See what we can do for you to bring the wow factor to your next event!</p>
    </div>
    <a class="search-button" href="#" aria-label="Search">
      <svg width="26" height="26" viewBox="0 0 26 26">
        <circle cx="10.5" cy="10.5" r="7.5" fill="none" stroke="#8e2a8c" stroke-width="4"/>
        <line x1="16" y1="16" x2="23" y2="23" stroke="#8e2a8c" stroke-width="4.5" stroke-linecap="round"/>
      </svg>
    </a>
    <div class="content-card side"></div>
    <div class="content-card wide"></div>
  </section>
</body>
</html>
```